Business Card Design

I want to pull elements/colors from Website. Attached is a screen shot. Do not want any buildings/building graphics/construction clichés. This is for a construction management firm but I want to keep it broad enough that I can expand into other areas. I do not want the logo to be limited. Thank you.
Updates

Please review the screen shot of the website. Please use the font and color of Brackwell Ventures, LLC on the website. Please use the tag line "Construction Management in the Palm Beaches" Please show contractor license ... CGC 4093615 You may use the back for the contact information. Please no phone/house icons. It does not have to be a black card. Thank you.

Target Market(s)

Professional people with money. Owners, Architects, Engineers, Developers, Real Estate Agents etc.

Industry/Entity Type

Construction

Contact Information for Business Card

Brackwell Ventures, LLC
Construction Management

Dale T Brackwell
240 Marlidge Court #14
Harbor Glen, FL 34990
(555) 555-0187
www.BrackwellVentures.example

Requirements
Must have
• Clean, crisp, modern.

Broad enough that it is not trapped into a particular industry.

My goal is to expand into different markets, different industries.

Should not have
• The back of the card should not be colored in any way. Rubs off on other cards.

Do not want any buildings/building graphics/construction clichés.

```html
<!DOCTYPE html>
<html lang="en">
<head>
<meta charset="utf-8">
<title>Brackwell Ventures – Business Card</title>
<link rel="stylesheet" href="https://fonts.googleapis.com/css2?family=Arimo:wght@400;700&display=swap">
<style>
  :root {
    --backdrop: #2b2b2b;
    --card: #ffffff;
    --brand-brown: #4a3436;
    --rule-mauve: #b9a5a8;
    --text-gray: #7a7576;
    --tag-gray: #a3a0a1;
  }
  html, body {
    margin: 0;
    width: 1200px;
    height: 1000px;
    overflow: hidden;
    background: var(--backdrop);
    font-family: "Arimo", Arial, sans-serif;
  }
  .card {
    position: absolute;
    left: 150px;
    top: 243px;
    width: 900px;
    height: 514px;
    background: var(--card);
    box-shadow: 0 10px 30px rgba(0,0,0,0.35);
  }
  .rule { position: absolute; }
  .rule--top, .rule--bottom {
    left: 0; right: 0; height: 2px; background: var(--brand-brown);
  }
  .rule--top { top: 56px; }
  .rule--bottom { top: 458px; }
  .rule--under-brand-short {
    left: 250px; width: 250px; top: 166px; height: 2px; background: var(--brand-brown);
  }
  .rule--under-brand-long {
    left: 250px; width: 470px; top: 180px; height: 1.5px; background: var(--rule-mauve);
  }
  .rule--under-name {
    left: 180px; width: 560px; top: 284px; height: 1.5px; background: var(--rule-mauve);
  }
  .rule--under-phone {
    left: 330px; width: 270px; top: 378px; height: 2px; background: var(--brand-brown);
  }
  .brand {
    position: absolute;
    left: 250px;
    top: 74px;
    display: flex;
    align-items: flex-start;
    gap: 16px;
  }
  .brand__mark {
    width: 44px; height: 44px; background: var(--brand-brown); margin-top: 2px;
  }
  .brand__name {
    color: var(--brand-brown);
    font-size: 38px;
    font-weight: 400;
    line-height: 1;
    letter-spacing: -0.5px;
  }
  .brand__tagline {
    color: var(--tag-gray);
    font-size: 19px;
    letter-spacing: 4.5px;
    text-transform: uppercase;
    margin-top: 6px;
  }
  .person {
    position: absolute;
    left: 0; right: 0;
    top: 214px;
    text-align: center;
    color: var(--brand-brown);
    font-size: 30px;
    font-weight: 700;
    letter-spacing: 14px;
    text-transform: uppercase;
  }
  .contact {
    position: absolute;
    left: 0; right: 0;
    text-align: center;
    margin: 0;
    line-height: 1.2;
  }
  .contact--address { top: 300px; color: var(--text-gray); font-size: 21px; letter-spacing: 1.5px; }
  .contact--phone { top: 336px; color: var(--brand-brown); font-size: 21px; letter-spacing: 3px; }
  .contact--web { top: 396px; color: var(--text-gray); font-size: 22px; letter-spacing: 2px; }
</style>
</head>
<body>
  <main class="card">
    <div class="rule rule--top"></div>

    <div class="brand">
      <div class="brand__mark"></div>
      <div class="brand__text">
        <div class="brand__name">Brackwell Ventures, LLC</div>
        <div class="brand__tagline">Construction Management</div>
      </div>
    </div>

    <div class="rule rule--under-brand-short"></div>
    <div class="rule rule--under-brand-long"></div>

    <div class="person">Dale T Brackwell</div>

    <div class="rule rule--under-name"></div>

    <p class="contact contact--address">240 Marlidge Court #14 Harbor Glen, FL 34990</p>
    <p class="contact contact--phone">(555) 555-0187</p>

    <div class="rule rule--under-phone"></div>

    <p class="contact contact--web">www.BrackwellVentures.example</p>

    <div class="rule rule--bottom"></div>
  </main>
</body>
</html>
```